New Woocommerce Design Project

We need a WooCommerce site design that reflects our personality as a young and stylish teenage 'athleisure' fashion brand. Our target market is young boys aged between 12 and 18 years old, who are sporty, cool, and fashion conscious. We would like to the site to feature large format photos of our products and models, as well as feature pages for product selection for purchase. This is a new company we are launching, so we are looking for a dynamic yet stylish design which is quick and easy to navigate and which will appeal to young people. We already have a logo which we will upload below. Our existing domain name is www.orbitwren.com. We would like the winning designer to code the website - if possible. We have uploaded some photos of the products currently being manufactured so you can see the type of design/style.

Target Market(s)

Teenage boys

Industry/Entity Type

Fashion

Coding

Coded - Design and coding required

Colors

Designer to choose colors to be used in the design.

Requirements
Must have
• Inclusion of logo, design must be stylish and contemporary. Colours must include white, logo background colour, and a dark navy blue.
Nice to have
• Inclusion of whole page photos of possible
Should not have
• Nothing that looks cheap or too childish.

```html
<!DOCTYPE html>
<html lang="en">
<head>
<meta charset="utf-8">
<title>Wren — Athleisure Collection</title>
<link rel="stylesheet" href="https://fonts.googleapis.com/css2?family=Open+Sans:wght@400;600;700&family=Bodoni+Moda:wght@700&family=Allura&display=swap">
<style>
:root{
  --taupe:#958a80;
  --taupe-light:#a89d94;
  --ink:#111111;
  --navy:#101b33;
  --white:#ffffff;
  --cream:#f8f6f2;
  --line:#d9d6d2;
  --star:#f2b41c;
  --muted:#6d6d6d;
}
*{margin:0;padding:0;box-sizing:border-box}
html,body{width:1200px;height:2725px;overflow:hidden}
body{position:relative;font-family:"Open Sans",sans-serif;color:var(--ink);background:var(--white)}
.abs{position:absolute}
.top-bar{left:0;top:0;width:1200px;height:30px;background:var(--taupe)}
.social{display:flex;gap:7px}
.social span{width:23px;height:23px;border-radius:50%;border:1.5px solid currentColor;display:flex;align-items:center;justify-content:center;font-size:7px;font-weight:700}
.top-social{left:112px;top:3px;color:var(--white)}
.account{right:112px;top:7px;color:var(--white);font-size:12px;display:flex;align-items:center;gap:6px}
.logo-tab{left:0;top:0}
.header{left:0;top:30px;width:1200px;height:46px;border-bottom:1px solid var(--line)}
.call{left:112px;top:40px;display:flex;gap:8px;align-items:center}
.call small{display:block;font-size:8px;color:var(--muted);letter-spacing:.5px}
.call b{display:block;font-size:11.5px;font-weight:400}
.logo{left:0;width:1200px;top:46px;text-align:center;font-size:17px;letter-spacing:3px;font-weight:600;color:var(--navy)}
.header-icons{right:112px;top:42px;display:flex;gap:16px}
.nav{left:0;top:76px;width:1200px;height:29px;display:flex;justify-content:center}
.nav a{font-size:12px;text-decoration:none;color:var(--ink);padding:6px 22px 0;height:29px}
.nav a.active{color:var(--taupe);border-bottom:2px solid var(--taupe)}
.hero-photo{left:0;top:105px;width:1200px;height:469px;background:linear-gradient(180deg,#ecebea 0%,#e6e4e2 62%,#dcc7bc 82%,#f1e6df 100%)}
.hero-subject{left:600px;top:105px;width:560px;height:469px;background:linear-gradient(160deg,#d9cdc0 0%,#6d7891 35%,#3f4e6a 60%,#d6d0ca 100%);opacity:.5;border-radius:50% 30% 0 45%}
.hero-title{left:113px;top:252px;font-family:"Bodoni Moda",serif;font-weight:700;font-size:54px;line-height:46px;letter-spacing:3px}
.hero-text{left:113px;top:350px;font-size:14.5px}
.btn{display:flex;align-items:center;justify-content:center;background:var(--navy);color:var(--white);font-size:12px;letter-spacing:.5px}
.hero-btn{left:113px;top:381px;width:120px;height:35px}
.perks{left:0;top:574px;width:1200px;height:75px;background:#f7f6f4;box-shadow:0 2px 3px rgba(0,0,0,.08)}
.perk{top:586px;display:flex;gap:12px;align-items:center;font-size:12px;line-height:15px}
.perk b{font-weight:700;letter-spacing:.5px}
.perk-divider{top:576px;width:1px;height:72px;background:var(--line)}
.section-cream{left:0;width:1200px;background:var(--cream)}
.section-title{left:0;width:1200px;text-align:center;font-size:18px;font-weight:700;letter-spacing:1.5px}
.card{width:181px;height:264px;background:var(--white);text-align:center}
.card .photo{width:181px;height:201px}
.card h3{font-size:11.5px;font-weight:700;margin-top:14px;letter-spacing:.5px}
.card p{font-size:16.5px;color:var(--muted);line-height:20px}
.card.framed{border:1px solid var(--line)}
.promo{left:0;top:1414px;width:1200px;height:252px;background:linear-gradient(90deg,#6f7979,#7d8787 55%,#737d7d)}
.promo-photo{left:635px;top:1425px;width:471px;height:241px;background:linear-gradient(180deg,#8c8f92 0%,#4d6380 45%,#31455f 100%);border-radius:120px 120px 0 0;opacity:.85}
.promo-script{left:152px;top:1468px;font-family:"Allura",cursive;font-size:50px;color:var(--white)}
.promo-sale{left:152px;top:1520px;font-family:"Bodoni Moda",serif;font-size:37px;color:var(--white);letter-spacing:2px}
.promo-off{left:152px;top:1560px;font-size:44px;font-weight:700;color:var(--white);letter-spacing:1px}
.review{top:2245px;width:429px;height:191px;background:var(--white);border:1px solid var(--line);text-align:center}
.avatar{top:2198px;width:94px;height:94px;border-radius:50%;border:1px solid var(--line)}
.review h4{font-size:14.5px;font-weight:700;margin-top:62px;letter-spacing:.5px}
.stars{display:flex;justify-content:center;margin:2px 0 5px}
.review p{font-size:12.5px;line-height:19px;padding:0 36px}
.arrow{top:2330px;width:22px;height:22px;border-radius:50%;background:var(--ink)}
.footer{left:0;top:2542px;width:1200px;height:183px;background:var(--navy)}
.foot-link{font-size:11.5px;color:var(--white)}
.email{left:736px;top:2597px;width:180px;height:28px;border:1px solid #cfcfcf;background:var(--white);font-size:12px;padding:6px 11px;color:var(--ink)}
.subscribe{left:923px;top:2597px;width:87px;height:28px;background:var(--taupe-light);color:var(--white);font-size:11.5px;display:flex;align-items:center;justify-content:center}
.foot-rule{left:112px;top:2690px;width:976px;height:1px;background:#3a4560}
.copyright{left:113px;top:2701px;font-size:11.5px;color:var(--white)}
.foot-logo{left:0;width:1200px;top:2697px;text-align:center;font-size:16px;letter-spacing:3px;font-weight:600;color:var(--white)}
.foot-social{right:112px;top:2696px;color:var(--white)}
</style>
</head>
<body>

<div class="abs top-bar"></div>
<div class="abs social top-social"><span>FB</span><span>IG</span><span>TW</span></div>
<div class="abs account">
  <svg width="12" height="12" viewBox="0 0 12 12" fill="#fff"><circle cx="6" cy="3.5" r="3"/><path d="M0 12c0-3.5 2.7-5 6-5s6 1.5 6 5z"/></svg>
  My Account
  <svg width="8" height="6" viewBox="0 0 8 6"><path d="M1 1l3 3 3-3" stroke="#fff" fill="none"/></svg>
</div>
<svg class="abs logo-tab" width="1200" height="31"><polygon points="518,31 534,0 666,0 682,31" fill="#fff"/></svg>

<div class="abs header"></div>
<div class="abs call">
  <svg width="22" height="22" viewBox="0 0 24 24" fill="none" stroke="#888" stroke-width="1.4"><path d="M5 3l4 1 1 5-2 1.5a12 12 0 006.5 6.5L16 15l5 1 1 4-2 2C10 22 2 14 2 4z"/></svg>
  <div><small>CALL US</small><b>(555) 014 2298</b></div>
</div>
<div class="abs logo">WREN</div>
<div class="abs header-icons">
  <svg width="18" height="18" viewBox="0 0 18 18" fill="none" stroke="#111" stroke-width="1.6"><circle cx="7.5" cy="7.5" r="6"/><path d="M12 12l5 5"/></svg>
  <svg width="18" height="18" viewBox="0 0 18 18" fill="none" stroke="#111" stroke-width="1.6"><path d="M9 16S1.5 11 1.5 6A3.7 3.7 0 019 4a3.7 3.7 0 017.5 2C16.5 11 9 16 9 16z"/></svg>
  <svg width="18" height="18" viewBox="0 0 18 18" fill="none" stroke="#111" stroke-width="1.6"><path d="M4 6h10v10H4z"/><path d="M6.5 6V4a2.5 2.5 0 015 0v2"/></svg>
</div>
<nav class="abs nav">
  <a class="active">HOME</a><a>ABOUT US</a><a>NEW COLLECTION</a><a>NEW ARRIVALS</a><a>REVIEWS</a><a>CONTACT US</a>
</nav>

<div class="abs hero-photo" role="img" aria-label="Boy in denim jacket and jeans sitting on a light floor"></div>
<div class="abs hero-subject" role="img" aria-label="Model wearing denim jacket, white tee and ripped jeans"></div>
<h1 class="abs hero-title">ATHLEISURE<br>COLLECTION</h1>
<p class="abs hero-text">Lorem ipsum dolor sit amet, consectetur adipiscing elit</p>
<div class="abs btn hero-btn">SHOP NOW</div>

<div class="abs perks"></div>
<div class="abs perk" style="left:180px">
  <svg width="30" height="34" viewBox="0 0 30 34" fill="#9c938b"><path d="M3 10h22l3 22H0z"/><path d="M9 10V6a5 5 0 0110 0v4" fill="none" stroke="#9c938b" stroke-width="2"/></svg>
  <div><b>FREE SHOPPING</b><br>Lorem ipsum dolor sit amet,<br>consectetur adipiscing elit</div>
</div>
<div class="abs perk-divider" style="left:438px"></div>
<div class="abs perk" style="left:496px">
  <svg width="34" height="34" viewBox="0 0 34 34" fill="#9c938b"><path d="M4 10l13-7 13 7v14l-13 7-13-7z"/><path d="M17 3v28M4 10l13 7 13-7" stroke="#f7f6f4" stroke-width="2" fill="none"/></svg>
  <div><b>30 DAYS RETURNS</b><br>Lorem ipsum dolor sit amet,<br>consectetur adipiscing elit</div>
</div>
<div class="abs perk-divider" style="left:758px"></div>
<div class="abs perk" style="left:816px">
  <svg width="36" height="30" viewBox="0 0 36 30" fill="#9c938b"><rect x="0" y="6" width="30" height="22" rx="2"/><rect x="0" y="11" width="30" height="4" fill="#f7f6f4"/><circle cx="28" cy="8" r="8"/><path d="M24 8l3 3 5-6" stroke="#f7f6f4" stroke-width="2" fill="none"/></svg>
  <div><b>100% PAYMENT SECURE</b><br>Lorem ipsum dolor sit amet,<br>consectetur adipiscing elit</div>
</div>

<div class="abs section-cream" style="top:649px;height:765px"></div>
<h2 class="abs section-title" style="top:692px">FEATURED PRODUCTS</h2>

<div class="abs card" style="left:194px;top:741px"><div class="photo" role="img" aria-label="Boy in teal track jacket and dark joggers" style="background:linear-gradient(180deg,#e4e4e4,#2a8a83 55%,#1f3a38)"></div><h3>RICKT SHIRT</h3><p>$120.50</p></div>
<div class="abs card" style="left:404px;top:741px"><div class="photo" role="img" aria-label="Boy in yellow tee, striped vest and sunglasses" style="background:linear-gradient(180deg,#dedede,#e9d93a 50%,#c8c8c8)"></div><h3>RICKT SHIRT</h3><p>$120.50</p></div>
<div class="abs card" style="left:615px;top:741px"><div class="photo" role="img" aria-label="Boy in cream fleece jacket sitting on a red court" style="background:linear-gradient(180deg,#a24a4a,#e0d9cc 50%,#b43b3e)"></div><h3>RICKT SHIRT</h3><p>$120.50</p></div>
<div class="abs card" style="left:825px;top:741px"><div class="photo" role="img" aria-label="Boy in white hoodie and mustard trousers" style="background:linear-gradient(180deg,#dbe8f0,#f1f1f1 45%,#cfa52a)"></div><h3>RICKT SHIRT</h3><p>$120.50</p></div>

<div class="abs card" style="left:194px;top:1036px"><div class="photo" role="img" aria-label="Boy in white tee and yellow shorts with skateboard" style="background:linear-gradient(180deg,#6fa8a8,#f2f2f2 45%,#e9d273 75%,#6fa8a8)"></div><h3>RICKT SHIRT</h3><p>$120.50</p></div>
<div class="abs card" style="left:404px;top:1036px"><div class="photo" role="img" aria-label="Two boys in red and blue tees on pink background" style="background:linear-gradient(180deg,#f5b0b5,#d9282c 35%,#2f5fb8 70%,#f5b0b5)"></div><h3>RICKT SHIRT</h3><p>$120.50</p></div>
<div class="abs card" style="left:615px;top:1036px"><div class="photo" role="img" aria-label="Boy in blue tee and khaki trousers on pink background" style="background:linear-gradient(180deg,#f5b4b9,#2f67c9 45%,#6d6b5e 80%,#f5b4b9)"></div><h3>RICKT SHIRT</h3><p>$120.50</p></div>
<div class="abs card" style="left:825px;top:1036px"><div class="photo" role="img" aria-label="Boy in light blue top and camo trousers on beige background" style="background:linear-gradient(180deg,#dcb998,#b7d4ef 45%,#8a8067 80%,#d8b491)"></div><h3>RICKT SHIRT</h3><p>$120.50</p></div>

<div class="abs btn" style="left:541px;top:1330px;width:119px;height:35px">VIEW ALL</div>

<div class="abs promo"></div>
<div class="abs promo-photo" role="img" aria-label="Four boys in denim jackets posing together"></div>
<div class="abs promo-script">Special Promo</div>
<div class="abs promo-sale">WEEKENDS SALE</div>
<div class="abs promo-off">UP TO 50% OFF</div>

<h2 class="abs section-title" style="top:1702px">NEW ARRIVALS</h2>
<div class="abs card framed" style="left:194px;top:1750px"><div class="photo" role="img" aria-label="Boy in red hoodie and cap on blue background" style="background:linear-gradient(180deg,#5b9fc2,#c4222b 45%,#24334a 85%)"></div><h3>RICKT SHIRT</h3><p>$120.50</p></div>
<div class="abs card framed" style="left:404px;top:1750px"><div class="photo" role="img" aria-label="Boy in yellow tee, striped vest and sunglasses" style="background:linear-gradient(180deg,#dedede,#e9d93a 50%,#c8c8c8)"></div><h3>RICKT SHIRT</h3><p>$120.50</p></div>
<div class="abs card framed" style="left:615px;top:1750px"><div class="photo" role="img" aria-label="Boy in green striped top on blue background" style="background:linear-gradient(180deg,#1486c6,#e8f1e8 45%,#2d9a48 60%,#2c4a7a 90%)"></div><h3>RICKT SHIRT</h3><p>$120.50</p></div>
<div class="abs card framed" style="left:825px;top:1750px"><div class="photo" role="img" aria-label="Boy in teal track jacket and dark joggers" style="background:linear-gradient(180deg,#e4e4e4,#2a8a83 55%,#1f3a38)"></div><h3>RICKT SHIRT</h3><p>$120.50</p></div>

<div class="abs btn" style="left:541px;top:2040px;width:119px;height:35px">VIEW ALL</div>

<div class="abs section-cream" style="top:2116px;height:426px"></div>
<h2 class="abs section-title" style="top:2157px">CUSTOMER TESTIMONIALS</h2>

<div class="abs arrow" style="left:113px"><svg width="22" height="22"><path d="M13 6l-5 5 5 5" stroke="#fff" stroke-width="2" fill="none"/></svg></div>
<div class="abs arrow" style="left:1066px"><svg width="22" height="22"><path d="M9 6l5 5-5 5" stroke="#fff" stroke-width="2" fill="none"/></svg></div>

<div class="abs review" style="left:162px">
  <h4>JOHN DOE</h4>
  <div class="stars"><svg width="144" height="20" viewBox="0 0 144 20" fill="#f2b41c"><g id="star"><path d="M10 0l3 6.5 7 .8-5.2 4.8 1.4 7L10 15.6 3.8 19l1.4-7L0 7.3l7-.8z"/></g><use href="#star" x="31"/><use href="#star" x="62"/><use href="#star" x="93"/><use href="#star" x="124"/></svg></div>
  <p>Lorem ipsum dolor sit amet, consectetur adipiscing elit. Nulla pharetra cursus augue eu semper. Sed mollis leo id mi efficitur, tincidunt faucibus nisi porttitor.</p>
</div>
<div class="abs avatar" style="left:329px;background:linear-gradient(180deg,#e9e9e9,#3e8fb0)" role="img" aria-label="Customer portrait, man in blue shirt and sunglasses"></div>

<div class="abs review" style="left:609px">
  <h4>JOHN DOE</h4>
  <div class="stars"><svg width="144" height="20" viewBox="0 0 144 20" fill="#f2b41c"><use href="#star"/><use href="#star" x="31"/><use href="#star" x="62"/><use href="#star" x="93"/><use href="#star" x="124"/></svg></div>
  <p>Lorem ipsum dolor sit amet, consectetur adipiscing elit. Nulla pharetra cursus augue eu semper. Sed mollis leo id mi efficitur, tincidunt faucibus nisi porttitor.</p>
</div>
<div class="abs avatar" style="left:776px;background:linear-gradient(180deg,#dcdcdc,#2c3e5c)" role="img" aria-label="Customer portrait, man in navy shirt"></div>

<div class="abs btn" style="left:541px;top:2461px;width:119px;height:35px">VIEW ALL</div>

<footer class="abs footer"></footer>
<div class="abs foot-link" style="left:189px;top:2571px">ABOUT US</div>
<div class="abs foot-link" style="left:189px;top:2602px">FIND A STORE</div>
<div class="abs foot-link" style="left:189px;top:2634px">SIZE GUIDE</div>
<div class="abs foot-link" style="left:339px;top:2571px">WHERE IS MY ORDER?</div>
<div class="abs foot-link" style="left:339px;top:2602px">FAQ</div>
<div class="abs foot-link" style="left:339px;top:2634px">TERMS AND CONDITIONS</div>
<div class="abs foot-link" style="left:551px;top:2571px">ABOUT BESTSELLER</div>
<div class="abs foot-link" style="left:551px;top:2602px">CONTACT US</div>
<div class="abs foot-link" style="left:551px;top:2634px">PRIVACY POLICY</div>
<div class="abs foot-link" style="left:733px;top:2571px">JOIN OUR NEWSLETTER NO</div>
<div class="abs email">Enter Email</div>
<div class="abs subscribe">SUBSCRIBE</div>
<div class="abs foot-rule"></div>
<div class="abs copyright">Copyright © 2010-2023</div>
<div class="abs foot-logo">WREN</div>
<div class="abs social foot-social"><span>FB</span><span>IG</span><span>TW</span></div>

</body>
</html>
```